Professional and creatice Life Coach - Business Card design

I just relaunched my website and now i a need a correspoonding business card for my task as life coach. My website is www.tbalrond.com as reference. The compass is kind of a symbol for my work, as I help people navigate through their challenging phases in life. The business card should be colorful, but not too playful as I also adress business people. So it sould be creative, but professional (also to suport my other business as Management Consultant)

Target Market(s)

People who want to get teir problems resolved, in business, partnership and other personal realms

Industry/Entity Type

Life Coaching

Contact Information for Business Card

Front side should include Name, Phone number, Email, Website and address

Font styles to use
Sans Serif

Colors
add136

Requirements
Must have
• "Mag. Leopold Brantner" -> Name
"Energetische Praxis" -> Jobtitle (describing my profession as life coach)
colours and style should match my website www.tbalrond.com
Nice to have
• a compass as a symbol

```html
<!DOCTYPE html>
<html lang="de">
<head>
<meta charset="utf-8">
<title>Leopold Brantner – Business Card</title>
<link href="https://fonts.googleapis.com/css2?family=Open+Sans:wght@400;600;700&display=swap" rel="stylesheet">
<style>
  :root {
    --bg: #1c1e21;
    --card: #262729;
    --accent: #add136;
    --text: #f2f2f2;
  }
  * { box-sizing: border-box; margin: 0; padding: 0; }
  html, body { width: 1200px; height: 900px; overflow: hidden; }
  body {
    background: var(--bg);
    font-family: "Open Sans", sans-serif;
    display: flex; align-items: center; justify-content: center; gap: 40px;
  }
  .card {
    position: relative; width: 540px; height: 310px;
    background: var(--card); border-radius: 18px; overflow: hidden;
    box-shadow: 0 10px 30px rgba(0,0,0,.45);
  }
  .card__strip { position: absolute; left: 0; top: 0; bottom: 0; width: 14px; background: var(--accent); }
  .brand { display: flex; align-items: center; gap: 10px; color: var(--accent); font-weight: 700; font-size: 22px; }
  .brand__dot { width: 26px; height: 26px; border-radius: 50%; background: var(--accent); flex: none; }
  .front .brand { position: absolute; left: 44px; top: 62px; }
  .front__divider { position: absolute; left: 200px; top: 118px; width: 3px; height: 150px; background: var(--accent); }
  .front__info { position: absolute; left: 222px; top: 38px; }
  .front__name { color: var(--accent); font-weight: 700; font-size: 25px; line-height: 1.2; }
  .front__title { color: var(--text); font-weight: 600; font-size: 16px; margin-bottom: 18px; }
  .contact { list-style: none; }
  .contact__item { display: flex; align-items: center; gap: 10px; color: var(--text); font-weight: 600; font-size: 14px; height: 32px; }
  .contact__icon { width: 22px; height: 22px; border-radius: 50%; background: var(--accent); display: flex; align-items: center; justify-content: center; flex: none; }
  .contact__icon svg { width: 12px; height: 12px; }
  .back .brand { position: absolute; left: 50%; top: 42%; transform: translate(-50%, -50%); font-size: 30px; }
  .back .brand__dot { width: 34px; height: 34px; }
  .back__web { position: absolute; left: 120px; bottom: 58px; color: var(--accent); font-size: 14px; font-weight: 600; }
</style>
</head>
<body>
  <section class="card front">
    <div class="card__strip"></div>
    <div class="brand"><span class="brand__dot"></span>Brantner</div>
    <div class="front__divider"></div>
    <div class="front__info">
      <h1 class="front__name">Mag. Leopold Brantner</h1>
      <p class="front__title">Energetische Praxis</p>
      <ul class="contact">
        <li class="contact__item"><span class="contact__icon"><svg viewBox="0 0 12 12"><path d="M2.5 1.5 L4.5 1.5 L5 4 L3.8 4.8 Q5 7.2 7.2 8.2 L8 7 L10.5 7.5 L10.5 9.5 Q6 10.5 3 7.5 Q1 5 2.5 1.5Z" fill="none" stroke="#262729" stroke-width="1.1"/></svg></span>+43 660 4827193</li>
        <li class="contact__item"><span class="contact__icon"><svg viewBox="0 0 12 12"><rect x="1.5" y="3" width="9" height="6.5" fill="none" stroke="#262729" stroke-width="1.1"/><path d="M1.5 3 L6 6.8 L10.5 3" fill="none" stroke="#262729" stroke-width="1.1"/></svg></span>leopold@brantner.one</li>
        <li class="contact__item"><span class="contact__icon"><svg viewBox="0 0 12 12"><circle cx="6" cy="6" r="4.5" fill="none" stroke="#262729" stroke-width="1.1"/><path d="M1.5 6 H10.5 M6 1.5 Q3.5 6 6 10.5 M6 1.5 Q8.5 6 6 10.5" fill="none" stroke="#262729" stroke-width="1"/></svg></span>www.tbalrond.com</li>
        <li class="contact__item"><span class="contact__icon"><svg viewBox="0 0 12 12"><path d="M6 11 Q2 6.5 2 4.5 A4 4 0 0 1 10 4.5 Q10 6.5 6 11Z" fill="none" stroke="#262729" stroke-width="1.1"/><circle cx="6" cy="4.6" r="1.4" fill="#262729"/></svg></span>Lindenweg 12, 5020 Salzburg, Austria</li>
      </ul>
    </div>
  </section>

  <section class="card back">
    <div class="brand"><span class="brand__dot"></span>Brantner</div>
    <p class="back__web">www.tbalrond.com</p>
  </section>
</body>
</html>
```